Traditional style Skull and crossbones craftsmans card for making custom works home decor and more

Brovick Forge surrounding a skull and cross bones. Street address is 417 Marlow Rd N Essex ON. Email is BrovickForge@mailnest.net and telephone number will be 555-314-9086. Use the attached image as a guideline would also like Support your local artist on the card. Our names are Dale and Morgan Brovick

Industry/Entity Type

It Support

Contact Information for Business Card

Standard size with a traditional style font

Font styles to use
Decorative
Script

Requirements
Must have
• 417 Marlow Rd. N Essex ON
• 555-314-9086
• Brovickforge@mailnest.net
• Welding
• Dale and Morgan Brovick
• Support your local artist
Nice to have
• Refer to images for ideas

```html
<!DOCTYPE html>
<html lang="en">
<head>
<meta charset="utf-8">
<title>Brovick Forge — Business Card</title>
<link href="https://fonts.googleapis.com/css2?family=Cinzel:wght@400;600;700&family=EB+Garamond:wght@400&display=swap" rel="stylesheet">
<style>
  :root {
    --orange: #f08000;
    --brown: #4f4039;
    --cream: #f3efe1;
    --cream-shade: #d9d3c0;
    --backdrop: #e6e6e6;
    --text-light: #f6f1e4;
    --text-dark: #4a3b33;
  }
  * { margin: 0; padding: 0; box-sizing: border-box; }
  html, body { width: 1200px; height: 702px; overflow: hidden; }
  body {
    background: var(--backdrop);
    font-family: "Cinzel", serif;
    position: relative;
  }
  .card {
    position: absolute;
    top: 196px;
    width: 540px;
    height: 310px;
    background: var(--orange);
    box-shadow: 0 6px 18px rgba(0,0,0,0.18);
    overflow: hidden;
  }
  /* Front */
  .card--front { left: 40px; }
  .side-strip {
    position: absolute;
    top: 0; bottom: 0;
    width: 30px;
    background: var(--cream);
    display: flex;
    align-items: center;
    justify-content: center;
  }
  .side-strip--left { left: 0; border-right: 3px solid var(--cream-shade); }
  .side-strip--right { right: 0; border-left: 3px solid var(--cream-shade); }
  .side-label {
    font-size: 11px;
    letter-spacing: 2px;
    color: var(--text-dark);
    white-space: nowrap;
  }
  .side-strip--left .side-label { transform: rotate(-90deg); }
  .side-strip--right .side-label { transform: rotate(90deg); }
  .brand {
    position: absolute;
    left: 30px; right: 30px; top: 0; bottom: 0;
    display: flex;
    flex-direction: column;
    align-items: center;
    justify-content: center;
    gap: 14px;
  }
  .brand-lockup {
    display: flex;
    align-items: center;
    gap: 16px;
  }
  .brand-mark {
    width: 22px; height: 22px;
    border-radius: 50%;
    background: var(--cream);
  }
  .brand-name {
    font-family: "Cinzel", serif;
    font-weight: 700;
    font-size: 44px;
    color: var(--cream);
    letter-spacing: 1px;
  }
  .brand-motto {
    font-size: 14px;
    letter-spacing: 2.4px;
    color: var(--text-light);
    text-transform: uppercase;
  }
  /* Back */
  .card--back { left: 620px; }
  .band {
    position: absolute;
    left: 0; right: 0;
    background: var(--brown);
    color: var(--text-light);
    display: flex;
    align-items: center;
    justify-content: center;
    white-space: nowrap;
  }
  .band--tagline { top: 9px; height: 37px; font-size: 19px; letter-spacing: 1.5px; }
  .band--trade { top: 205px; height: 37px; font-size: 14px; letter-spacing: 1.6px; }
  .band--services { top: 268px; height: 39px; font-size: 19px; letter-spacing: 2.4px; gap: 14px; }
  .rule {
    position: absolute;
    left: 0; right: 0;
    height: 4px;
    background: var(--brown);
  }
  .rule--top { top: 54px; }
  .rule--upper { top: 184px; }
  .rule--lower { top: 251px; }
  .bullet {
    width: 7px; height: 7px;
    border-radius: 50%;
    background: var(--orange);
    display: inline-block;
  }
  .contact {
    position: absolute;
    top: 65px; left: 0; right: 0;
    text-align: center;
    color: var(--text-light);
    font-style: normal;
  }
  .contact-names { font-size: 13px; font-weight: 600; letter-spacing: 1.4px; line-height: 19px; }
  .contact-line { font-size: 14px; letter-spacing: 1px; line-height: 17px; }
  .contact-phone { font-size: 20px; letter-spacing: 1.5px; line-height: 25px; }
  .contact-email { font-family: "EB Garamond", serif; font-size: 14px; letter-spacing: 0.6px; line-height: 18px; }
</style>
</head>
<body>
  <section class="card card--front" aria-label="Card front">
    <div class="side-strip side-strip--left"><span class="side-label">DESIGNER</span></div>
    <div class="brand">
      <div class="brand-lockup">
        <span class="brand-mark"></span>
        <span class="brand-name">Brovick Forge</span>
      </div>
      <div class="brand-motto">Support your local artist</div>
    </div>
    <div class="side-strip side-strip--right"><span class="side-label">CRAFTSMAN</span></div>
  </section>

  <section class="card card--back" aria-label="Card back">
    <div class="band band--tagline">Specializing In “ One Of a Kind” Designs</div>
    <div class="rule rule--top"></div>
    <address class="contact">
      <div class="contact-names">Dale and Morgan Brovick</div>
      <div class="contact-line">417 Marlow RD.N</div>
      <div class="contact-line">ESSEX.ON</div>
      <div class="contact-line">N8M 2K4</div>
      <div class="contact-phone">555 314 9086</div>
      <div class="contact-email">BrovickForge@mailnest.net</div>
    </address>
    <div class="rule rule--upper"></div>
    <div class="band band--trade">BLACKSMITHING &amp; CUSTOM WELDING</div>
    <div class="rule rule--lower"></div>
    <div class="band band--services">
      <span class="bullet"></span>DESIGNING
      <span class="bullet"></span>BUILDING
      <span class="bullet"></span>SCULPTING
      <span class="bullet"></span>
    </div>
  </section>
</body>
</html>
```